Spy/Espionage/Counterintelligence Membership Community Needs a PowerPoint Template

We need a powerpoint template for one of our business verticals focused on spies, espionage, and counterintelligence. The name of it is "Amber Harbor Guild" and the logo is attached. Amber Harbor Guild is a community that connects people with experts in espionage and counterintelligence through an online social network, as well as in-person events. We would like to see designs that incorporate the red and black of the logo. The design should communicate mystery/suspense and peak curiosity.

Target Market(s)

Late 20s to baby boomers, male

Industry/Entity Type

Social Club

Font styles to use
Sans Serif

Colors
ec1f27
000000
ffffff

Requirements
Must have
• A user-friendly ppt template file. Incorporate basic fonts that don't have to be installed on every computer for presentations. A cover slide and a basic inside slide. A white background. I will also need graphic source files.
Nice to have
• Plenty of space for slide title and body content. Logo on every slide.
Should not have
• Inconsistency with fonts. Misalignment of images.

```html
<!DOCTYPE html>
<html lang="en">
<head>
<meta charset="utf-8">
<title>Amber Harbor Guild – Presentation Template</title>
<link rel="stylesheet" href="https://fonts.googleapis.com/css2?family=Figtree:wght@400;600;700;800&display=swap">
<style>
:root{
  --red:#ec1f27;
  --red-soft:#f2545a;
  --black:#000000;
  --charcoal:#2b2b2b;
  --charcoal-2:#3d3d3d;
  --footer:#262626;
  --white:#ffffff;
  --paper:#ffffff;
  --paper-shade:#dedede;
  --ink:#333333;
  --grey:#9a9a9a;
  --grey-light:#cfcfcf;
  --row:#f3f3f3;
}
*{box-sizing:border-box;margin:0;padding:0}
html,body{width:1061px;height:1200px;overflow:hidden;background:var(--black)}
body{font-family:"Figtree",Arial,sans-serif;color:var(--ink)}
.sheet{
  width:1061px;height:1200px;padding:8px;
  display:grid;grid-template-columns:518px 518px;grid-template-rows:388px 388px 388px;gap:9px;
}
.slide{position:relative;overflow:hidden;background:linear-gradient(160deg,var(--paper) 30%,var(--paper-shade));}
.slide::before{content:"";position:absolute;left:0;top:0;right:0;height:9px;background:var(--red)}
.slide--dark{background:linear-gradient(135deg,var(--charcoal-2),var(--charcoal) 60%,#1f1f1f)}

/* footer */
.footer{position:absolute;left:0;right:0;bottom:0;height:40px;background:var(--footer);
  display:flex;align-items:center;justify-content:space-between;padding:0 22px 0 22px;color:var(--white)}
.slide--inner .footer{border-top:4px solid var(--red);height:42px}
.brand{display:flex;align-items:center;gap:8px;font-size:18px;font-weight:400;color:var(--white);letter-spacing:-.2px}
.brand-dot{width:24px;height:24px;border-radius:50%;border:2px solid var(--white)}
.pager{display:flex;align-items:center;gap:6px;font-size:13px;color:var(--white)}
.pager svg{display:block}
.pager .sep{width:1px;height:20px;background:#777;margin:0 10px 0 8px}

/* cover + closing */
.band{position:absolute;left:0;right:0;top:291px;height:49px;background:var(--red)}
.footer--cover{height:48px}
.byline{text-align:right;font-size:13px;line-height:1.25;color:var(--white)}
.byline b{display:block;color:var(--red);font-weight:700;font-size:14px}
.cover-title{position:absolute;left:46px;top:58px;color:var(--white)}
.cover-title .l1{font-size:47px;font-weight:800;line-height:1;color:var(--red)}
.cover-title .l2{font-size:47px;font-weight:800;line-height:1;margin-top:2px}
.cover-title .l3{font-size:25px;font-weight:400;margin-top:2px}
.cover-title .l3 span{color:var(--red)}
.cover-title p{font-size:12.5px;line-height:1.4;margin-top:10px;width:330px}
.chevron{position:absolute;left:418px;top:73px}
.thanks{position:absolute;right:34px;top:54px;text-align:right;font-weight:800;font-size:72px;line-height:.92;color:var(--white)}
.thanks span{color:var(--red);display:block}

/* inner */
.heading{position:absolute;left:22px;top:22px;font-size:29px;font-weight:700;color:var(--ink)}
.heading span{color:var(--red)}
.about{position:absolute;left:22px;top:74px;right:22px;font-size:13.4px;line-height:1.38;text-align:justify;color:#3a3a3a}
.about p{margin-bottom:11px}
.about b{color:var(--red);font-weight:600}
.services{position:absolute;left:42px;top:72px;list-style:none}
.services li{font-size:18px;font-weight:600;color:var(--ink);line-height:25px;display:flex;align-items:center;gap:12px}
.services li::before{content:"";width:6px;height:6px;background:var(--red);transform:rotate(45deg)}
.team-photo{position:absolute;left:228px;top:83px;width:260px;height:218px;border-radius:4px;
  background:linear-gradient(180deg,#cfcfcf,#5a5a5a 45%,#2a2a2a)}

.grid-table{position:absolute;left:25px;top:74px;width:470px;border-collapse:collapse;font-size:9.5px}
.grid-table th{height:25px;font-size:14px;font-weight:700}
.grid-table th.cat{background:var(--grey);color:var(--ink);width:233px}
.grid-table th.o1{background:var(--red);color:var(--white);width:118px}
.grid-table th.o2{background:#3a3a3a;color:var(--white)}
.grid-table tr.group td{background:var(--grey-light);font-weight:700;font-size:10.5px;padding:3px 0 2px;height:18px}
.grid-table td{height:18px;padding-left:0}
.grid-table td.item{padding-left:28px;background:var(--white);color:#555}
.grid-table tr.alt td.item{background:var(--row)}
.grid-table td.y{background:var(--red);color:var(--white);text-align:center}
.grid-table tr.alt td.y{background:var(--red-soft)}
.grid-table td.n{background:#3f3f3f;color:var(--white);text-align:center}
.grid-table tr.alt td.n{background:#5e5e5e}

.map{position:absolute;left:32px;top:73px;width:229px;height:222px;border:4px solid var(--white);
  box-shadow:0 0 0 1px #ccc;background:linear-gradient(135deg,#d9e4b8,#c4d39a 45%,#9cc3d8)}
.contact{position:absolute;left:274px;top:72px;width:228px;font-size:9.5px;line-height:1.3;color:#444}
.contact p.intro{text-align:justify;margin-bottom:8px}
.contact p.intro b{color:var(--red);font-weight:600}
.contact h4{color:var(--red);font-size:11.5px;font-weight:700;margin-top:7px}
.social{position:absolute;left:42px;top:312px;display:flex;align-items:center;gap:8px;font-size:11px;font-weight:600;color:var(--ink)}
.social i{width:17px;height:17px;background:var(--red);border-radius:2px}
.social span{margin-left:2px}
.social em{font-style:normal;color:var(--red)}
</style>
</head>
<body>
<main class="sheet">

  <!-- Cover -->
  <section class="slide slide--dark">
    <div class="cover-title">
      <div class="l1">TITLE</div>
      <div class="l2">PROJECT</div>
      <div class="l3">subtext <span>presentation</span></div>
      <p>Lorem ipsum dolor sit amet, consectetuer adipiscing elit. Maecenas porttitor congue massa.</p>
    </div>
    <svg class="chevron" width="56" height="106" viewBox="0 0 56 106" aria-hidden="true">
      <polygon points="0,0 56,53 0,106 20,53" fill="#ffffff"/>
    </svg>
    <div class="band"></div>
    <footer class="footer footer--cover">
      <div class="brand"><span class="brand-dot"></span>Amber Harbor Guild</div>
      <div class="byline">Presentation by<b>Daniel Reeve</b></div>
    </footer>
  </section>

  <!-- About -->
  <section class="slide slide--inner">
    <h2 class="heading"><span>About</span> Company</h2>
    <div class="about">
      <p><b>Lorem ipsum</b> dolor sit amet, consectetuer adipiscing elit. Maecenas porttitor congue massa. Fusce posuere, magna sed pulvinar ultricies, purus lectus malesuada libero, sit amet commodo magna eros quis urna.</p>
      <p><b>Nunc viverra imperdiet enim</b>. Fusce est. Vivamus a tellus. Pellentesque habitant morbi tristique senectus et netus et malesuada fames ac turpis egestas. Proin pharetra nonummy pede. Mauris et orci.</p>
      <p><b>Aenean nec lorem.</b> In porttitor. Donec laoreet nonummy augue.</p>
      <p>Suspendisse dui purus, scelerisque at, vulputate vitae, pretium mattis, nunc. Mauris eget neque at sem venenatis eleifend. Ut nonummy.</p>
      <p><b>Fusce aliquet pede non pede.</b><br>Suspendisse dapibus lorem pellentesque magna. Integer nulla.</p>
    </div>
    <footer class="footer">
      <div class="brand">Amber Harbor Guild</div>
      <div class="pager">
        <svg width="22" height="20" viewBox="0 0 22 20"><rect width="22" height="20" rx="3" fill="#ec1f27"/><path d="M13 5 8 10l5 5" stroke="#fff" stroke-width="2.5" fill="none"/></svg>
        <svg width="22" height="20" viewBox="0 0 22 20"><rect width="22" height="20" rx="3" fill="#ec1f27"/><path d="M9 5l5 5-5 5" stroke="#fff" stroke-width="2.5" fill="none"/></svg>
        <span class="sep"></span>2
      </div>
    </footer>
  </section>

  <!-- Services -->
  <section class="slide slide--inner">
    <h2 class="heading"><span>Our</span> Services</h2>
    <ul class="services">
      <li>Lorem ipsum</li><li>Lorem ipsum</li><li>Lorem ipsum</li><li>Lorem ipsum</li><li>Lorem ipsum</li>
      <li>Lorem ipsum</li><li>Lorem ipsum</li><li>Lorem ipsum</li><li>Lorem ipsum</li><li>Lorem ipsum</li>
    </ul>
    <div class="team-photo" role="img" aria-label="Photo of a group of business people in suits standing together"></div>
    <footer class="footer">
      <div class="brand">Amber Harbor Guild</div>
      <div class="pager">
        <svg width="22" height="20" viewBox="0 0 22 20"><rect width="22" height="20" rx="3" fill="#ec1f27"/><path d="M13 5 8 10l5 5" stroke="#fff" stroke-width="2.5" fill="none"/></svg>
        <svg width="22" height="20" viewBox="0 0 22 20"><rect width="22" height="20" rx="3" fill="#ec1f27"/><path d="M9 5l5 5-5 5" stroke="#fff" stroke-width="2.5" fill="none"/></svg>
        <span class="sep"></span>3
      </div>
    </footer>
  </section>

  <!-- Table -->
  <section class="slide slide--inner">
    <h2 class="heading"><span>Table</span> Presentation</h2>
    <table class="grid-table">
      <thead><tr><th class="cat">CATEGORY</th><th class="o1">OPTION 1</th><th class="o2">OPTION 2</th></tr></thead>
      <tbody>
        <tr class="group"><td colspan="3">&nbsp; Category 1</td></tr>
        <tr><td class="item">Lorem ipsum dolor sit amet</td><td class="y">Yes</td><td class="n">-</td></tr>
        <tr class="alt"><td class="item">Lorem ipsum dolor sit amet</td><td class="y">Yes</td><td class="n">-</td></tr>
        <tr><td class="item">Lorem ipsum dolor sit amet</td><td class="y">Yes</td><td class="n">-</td></tr>
        <tr class="group"><td colspan="3">&nbsp; Category 2</td></tr>
        <tr><td class="item">Lorem ipsum dolor sit amet</td><td class="y">Yes</td><td class="n">-</td></tr>
        <tr class="alt"><td class="item">Lorem ipsum dolor sit amet</td><td class="y">Yes</td><td class="n">-</td></tr>
        <tr><td class="item">Lorem ipsum dolor sit amet</td><td class="y">Yes</td><td class="n">-</td></tr>
        <tr class="alt"><td class="item">Lorem ipsum dolor sit amet</td><td class="y">Yes</td><td class="n">-</td></tr>
        <tr class="group"><td colspan="3">&nbsp; Category 3</td></tr>
        <tr><td class="item">Lorem ipsum dolor sit amet</td><td class="y">Yes</td><td class="n">-</td></tr>
        <tr class="alt"><td class="item">Lorem ipsum dolor sit amet</td><td class="y">Yes</td><td class="n">-</td></tr>
      </tbody>
    </table>
    <footer class="footer">
      <div class="brand">Amber Harbor Guild</div>
      <div class="pager">
        <svg width="22" height="20" viewBox="0 0 22 20"><rect width="22" height="20" rx="3" fill="#ec1f27"/><path d="M13 5 8 10l5 5" stroke="#fff" stroke-width="2.5" fill="none"/></svg>
        <svg width="22" height="20" viewBox="0 0 22 20"><rect width="22" height="20" rx="3" fill="#ec1f27"/><path d="M9 5l5 5-5 5" stroke="#fff" stroke-width="2.5" fill="none"/></svg>
        <span class="sep"></span>4
      </div>
    </footer>
  </section>

  <!-- Contact -->
  <section class="slide slide--inner">
    <h2 class="heading"><span>Contact</span> Info</h2>
    <div class="map" role="img" aria-label="Map of Europe and the Mediterranean region"></div>
    <div class="contact">
      <p class="intro"><b>Lorem ipsum</b> dolor sit amet, consectetuer adipiscing elit. Maecenas porttitor congue massa. Fusce posuere, magna sed pulvinar ultricies, purus lectus malesuada libero, sit amet commodo magna eros quis urna.</p>
      <h4>Address</h4>
      <p>58 Quayside Lane<br>Portland, Maine<br>04101 (U.S.A)</p>
      <h4>Phone</h4><p>0198-555-214</p>
      <h4>FAX</h4><p>0198-555-214</p>
      <h4>Email</h4><p>info@harborguild.example</p>
      <h4>Website</h4><p>www.harborguild.example</p>
    </div>
    <div class="social"><i></i><i></i><i></i><i></i><span>@HARBOR<em>GUILD</em></span></div>
    <footer class="footer">
      <div class="brand">Amber Harbor Guild</div>
      <div class="pager">
        <svg width="22" height="20" viewBox="0 0 22 20"><rect width="22" height="20" rx="3" fill="#ec1f27"/><path d="M13 5 8 10l5 5" stroke="#fff" stroke-width="2.5" fill="none"/></svg>
        <svg width="22" height="20" viewBox="0 0 22 20"><rect width="22" height="20" rx="3" fill="#ec1f27"/><path d="M9 5l5 5-5 5" stroke="#fff" stroke-width="2.5" fill="none"/></svg>
        <span class="sep"></span>5
      </div>
    </footer>
  </section>

  <!-- Closing -->
  <section class="slide slide--dark">
    <div class="thanks"><span>Thank</span>You</div>
    <div class="band"></div>
    <footer class="footer footer--cover">
      <div class="brand"><span class="brand-dot"></span>Amber Harbor Guild</div>
      <div class="byline">Presentation by<b>Daniel Reeve</b></div>
    </footer>
  </section>

</main>
</body>
</html>
```